pressure washing advertisment

I would like front and back designed post cards. we offer pressure washing services for residential customers. I want to highlight before and after pictures as examples of our more popular services. I would also like to have our email www.bluhavenwashco.example and the facebook and Instagram logo somewhere. you can also include all major credit card logos as acceptable payments. I have attached our logo along with before and after pictures. also feel free to go to my website for any additional information that should be added to the post card. lastly I want a small promotion of $25 off any service somewhere.<br/><br/>Thank you!!

Target Market(s)

homeowners

Industry/Entity Type

Cleaning Service

Font styles to use
Serif
Sans Serif

Colors

Designer to choose colors to be used in the design.

Requirements
Must have
• before and after pictures with website and logo
Nice to have
• clean look that flows

```html
<!DOCTYPE html>
<html lang="en">
<head>
<meta charset="utf-8">
<title>Bluhaven Wash Co – Postcard Front and Back</title>
<link rel="stylesheet" href="https://fonts.googleapis.com/css2?family=Barlow:wght@400;600;700&family=Barlow+Condensed:ital,wght@0,600;0,700;1,600;1,700&family=Roboto+Slab:wght@700;800&display=swap">
<style>
  :root{
    --navy:#1d3f77;
    --navy-deep:#16315f;
    --red:#e31e26;
    --white:#ffffff;
    --mist:#eef0f4;
    --ink:#2b2f38;
    --backdrop:#d9dadd;
  }
  *{box-sizing:border-box;margin:0;padding:0}
  html,body{width:940px;height:1200px;overflow:hidden;background:var(--backdrop)}
  body{position:relative;font-family:"Barlow",Arial,sans-serif}

  .postcard{position:absolute;left:40px;width:860px;height:572px;overflow:hidden;background:var(--mist);box-shadow:0 4px 14px rgba(0,0,0,.25)}
  .postcard--front{top:22px}
  .postcard--back{top:608px}

  .backdrop-photo{position:absolute;inset:0;background:linear-gradient(120deg,#f3f4f7 0%,#e4e7ee 35%,#f0e4e6 60%,#f4f5f8 100%)}

  /* Front */
  .brand-name{position:absolute;left:34px;top:62px;font-family:"Barlow",sans-serif;font-weight:700;color:var(--navy);font-size:46px;line-height:1.02;letter-spacing:.5px}
  .headline-band{position:absolute;left:0;top:222px;width:860px;height:167px;background:var(--navy)}
  .headline-band__kicker{position:absolute;left:32px;top:18px;font-family:"Barlow Condensed",sans-serif;font-style:italic;font-weight:600;font-size:28px;color:var(--white)}
  .headline-band__title{position:absolute;left:32px;top:44px;font-family:"Barlow Condensed",sans-serif;font-weight:700;font-size:66px;color:var(--white);letter-spacing:.5px}
  .headline-band__place{position:absolute;left:32px;top:112px;font-family:"Barlow Condensed",sans-serif;font-style:italic;font-weight:600;font-size:31px;letter-spacing:2px;color:var(--white)}

  .promise{position:absolute;left:0;top:389px;width:860px;height:78px;background:var(--white)}
  .promise__text{position:absolute;left:32px;top:6px;font-family:"Barlow Condensed",sans-serif;font-style:italic;font-weight:700;color:var(--red);font-size:24px;line-height:30px}
  .promise__text strong{font-size:31px}

  .services-band{position:absolute;left:0;top:500px;width:860px;height:72px;background:var(--red)}
  .services-tab{position:absolute;z-index:2;left:0;top:465px;height:36px;width:575px;background:var(--navy);clip-path:polygon(0 0,100% 0,96% 100%,0 100%);color:var(--white);font-family:"Barlow Condensed",sans-serif;font-weight:600;font-size:25px;line-height:36px;padding-left:32px}
  .services-list{position:absolute;left:32px;top:8px;list-style:none;display:grid;grid-template-columns:340px 320px;row-gap:2px;font-family:"Barlow Condensed",sans-serif;font-weight:600;font-size:23px;color:var(--white)}
  .services-list li::before{content:"";display:inline-block;width:6px;height:9px;border-radius:3px;background:var(--white);margin-right:7px;vertical-align:2px}

  .result-photo{position:absolute;border-radius:50%;overflow:hidden;border:3px solid var(--white)}
  .result-photo__image{position:absolute;inset:0}
  .result-photo__image--before{background:linear-gradient(160deg,#a9b8c9 0%,#cfc39c 40%,#b8ad85 70%,#5f7a3b 100%)}
  .result-photo__image--after{background:linear-gradient(160deg,#8fb1de 0%,#f1eccf 40%,#e7e1c2 70%,#6f8f44 100%)}
  .result-photo__image--lawn-before{background:linear-gradient(150deg,#b47a45 0%,#9fae6a 40%,#6e8d3c 100%)}
  .result-photo__image--lawn-after{background:linear-gradient(150deg,#f2f2ef 0%,#d9dcd6 40%,#7a9a45 100%)}
  .result-photo__image--porch-before{background:linear-gradient(170deg,#c9ccd2 0%,#8a8f8f 45%,#5d605e 100%)}
  .result-photo__image--porch-after{background:linear-gradient(170deg,#d8dde5 0%,#eef0f2 45%,#9aa0a6 100%)}
  .result-photo__label{position:absolute;left:0;right:0;bottom:0;font-family:"Roboto Slab",serif;font-weight:800;font-size:17px;color:var(--white);text-align:center;letter-spacing:.5px}
  .result-photo__label--navy{background:var(--navy)}
  .result-photo__label--red{background:var(--red)}

  .offer-badge{position:absolute}
  .offer-badge svg{display:block}
  .offer-badge text{font-family:"Roboto Slab",serif;fill:var(--white)}
  .offer-badge__amount{font-weight:800}
  .offer-badge__note{font-weight:700}

  /* Back */
  .about__title{position:absolute;left:45px;top:52px;font-family:"Barlow",sans-serif;font-weight:700;font-size:28px;color:var(--navy)}
  .about__copy{position:absolute;left:45px;top:96px;width:540px;font-size:18.5px;line-height:24px;color:var(--ink);white-space:nowrap}
  .benefits{position:absolute;left:45px;top:300px;list-style:none;font-family:"Barlow",sans-serif;font-weight:600;font-size:21.5px;line-height:26.5px;color:var(--navy)}
  .benefits li{display:flex;align-items:center;gap:6px}
  .stamp-box{position:absolute;left:717px;top:56px;width:106px;height:106px;background:var(--red)}

  .contact-band{position:absolute;left:0;top:480px;width:860px;height:92px;background:var(--red)}
  .call-tab{position:absolute;z-index:2;left:0;top:444px;height:45px;width:576px;background:var(--navy);clip-path:polygon(0 0,97% 0,100% 100%,0 100%);color:var(--white);font-family:"Barlow",sans-serif;font-weight:600;font-size:31px;line-height:45px;padding-left:45px;white-space:nowrap}
  .contact-band__lines{position:absolute;left:45px;top:16px;font-family:"Barlow",sans-serif;font-weight:600;font-size:22px;line-height:29px;color:var(--white)}
  .social-dot{position:absolute;top:21px;width:54px;height:54px;border-radius:50%;background:var(--navy);border:2px solid var(--white)}
</style>
</head>
<body>

<section class="postcard postcard--front" aria-label="Postcard front">
  <div class="backdrop-photo" role="img" aria-label="Faded waving flag photo background"></div>

  <div class="brand-name">BLUHAVEN<br>WASH CO</div>

  <div class="headline-band">
    <div class="headline-band__kicker">PROFESSIONAL RESIDENTIAL &amp; COMMERCIAL</div>
    <div class="headline-band__title">PRESSURE WASHING</div>
    <div class="headline-band__place">CONTRACTOR IN ST. AUGUSTINE, FL</div>
  </div>

  <div class="promise">
    <p class="promise__text">We Offer Pressure And Soft Washing Services<br>That Allow Us To Protect Your <strong>#1 Investment.</strong></p>
  </div>

  <div class="services-band">
    <ul class="services-list">
      <li>Soft Wash House Washing</li>
      <li>Gutter Cleaning &amp; Brightening</li>
      <li>Driveway &amp; Concrete Cleaning</li>
      <li>Deck &amp; Fence Washing</li>
    </ul>
  </div>
  <div class="services-tab">RESIDENTIAL PRESSURE WASHING SERVICES</div>

  <div class="result-photo" style="left:691px;top:160px;width:200px;height:200px">
    <div class="result-photo__image result-photo__image--lawn-after" role="img" aria-label="After photo: clean white foundation wall above green lawn"></div>
    <div class="result-photo__label result-photo__label--red" style="height:34px;line-height:30px">AFTER</div>
  </div>
  <div class="result-photo" style="left:549px;top:158px;width:178px;height:178px">
    <div class="result-photo__image result-photo__image--lawn-before" role="img" aria-label="Before photo: stained foundation wall above green lawn"></div>
    <div class="result-photo__label result-photo__label--red" style="height:36px;line-height:30px">BEFORE</div>
  </div>
  <div class="result-photo" style="left:659px;top:0;width:200px;height:200px">
    <div class="result-photo__image result-photo__image--after" role="img" aria-label="After photo: clean yellow house siding with pressure washer wand"></div>
    <div class="result-photo__label result-photo__label--navy" style="height:40px;line-height:34px">AFTER</div>
  </div>
  <div class="result-photo" style="left:479px;top:0;width:200px;height:200px">
    <div class="result-photo__image result-photo__image--before" role="img" aria-label="Before photo: mildewed yellow house siding with pressure washer wand"></div>
    <div class="result-photo__label result-photo__label--navy" style="height:40px;line-height:34px">BEFORE</div>
  </div>

  <div class="offer-badge" style="left:662px;top:388px">
    <svg width="160" height="160" viewBox="0 0 160 160" aria-label="$25 off any service">
      <path d="M 80 4 A 76 76 0 0 1 152 60" fill="none" stroke="#1d3f77" stroke-width="4"/>
      <path d="M 154 80 A 74 74 0 0 1 100 152" fill="none" stroke="#1d3f77" stroke-width="4"/>
      <circle cx="80" cy="80" r="68" fill="#1d3f77"/>
      <text class="offer-badge__amount" x="80" y="88" text-anchor="middle" font-size="50">$25</text>
      <text class="offer-badge__note" x="80" y="112" text-anchor="middle" font-size="19">OFF any</text>
      <text class="offer-badge__note" x="80" y="128" text-anchor="middle" font-size="16">service</text>
    </svg>
  </div>
</section>

<section class="postcard postcard--back" aria-label="Postcard back">
  <div class="backdrop-photo" role="img" aria-label="Faded flag and sky photo background"></div>

  <h2 class="about__title">ABOUT BLUHAVEN WASH CO</h2>
  <p class="about__copy">Since our founding, we’ve worked with numerous clients<br>throughout the area. Great service begins and ends with<br>experienced and friendly professionals, which is why we put so<br>much consideration into the quality of our work and our<br>customer's satisfaction. We complete projects efficiently and<br>on schedule, and go above and beyond to form lasting<br>relationships with our clients.</p>

  <ul class="benefits">
    <li><svg width="20" height="20" viewBox="0 0 20 20"><circle cx="10" cy="10" r="8" fill="none" stroke="#e31e26" stroke-width="2.2"/><path d="M6 10.5l3 3 6-7" fill="none" stroke="#e31e26" stroke-width="2.4"/></svg>Experienced &amp; Friendly Professionals</li>
    <li><svg width="20" height="20" viewBox="0 0 20 20"><circle cx="10" cy="10" r="8" fill="none" stroke="#e31e26" stroke-width="2.2"/><path d="M6 10.5l3 3 6-7" fill="none" stroke="#e31e26" stroke-width="2.4"/></svg>Free Estimates</li>
    <li><svg width="20" height="20" viewBox="0 0 20 20"><circle cx="10" cy="10" r="8" fill="none" stroke="#e31e26" stroke-width="2.2"/><path d="M6 10.5l3 3 6-7" fill="none" stroke="#e31e26" stroke-width="2.4"/></svg>100% Satisfaction Guaranteed</li>
    <li><svg width="20" height="20" viewBox="0 0 20 20"><circle cx="10" cy="10" r="8" fill="none" stroke="#e31e26" stroke-width="2.2"/><path d="M6 10.5l3 3 6-7" fill="none" stroke="#e31e26" stroke-width="2.4"/></svg>Residential &amp; Commercial</li>
  </ul>

  <div class="offer-badge" style="left:540px;top:32px">
    <svg width="140" height="140" viewBox="0 0 140 140" aria-label="$25 off any service">
      <path d="M 70 4 A 66 66 0 0 1 133 55" fill="none" stroke="#1d3f77" stroke-width="3.5"/>
      <path d="M 135 72 A 64 64 0 0 1 88 132" fill="none" stroke="#1d3f77" stroke-width="3.5"/>
      <circle cx="70" cy="70" r="58" fill="#1d3f77"/>
      <text class="offer-badge__amount" x="70" y="77" text-anchor="middle" font-size="43">$25</text>
      <text class="offer-badge__note" x="70" y="98" text-anchor="middle" font-size="16">OFF any</text>
      <text class="offer-badge__note" x="70" y="112" text-anchor="middle" font-size="14">service</text>
    </svg>
  </div>

  <div class="stamp-box"></div>

  <div class="result-photo" style="left:564px;top:183px;width:152px;height:152px">
    <div class="result-photo__image result-photo__image--porch-before" role="img" aria-label="Before photo: grimy covered porch ceiling and siding"></div>
    <div class="result-photo__label result-photo__label--red" style="height:28px;line-height:24px;font-size:15px">BEFORE</div>
  </div>
  <div class="result-photo" style="left:423px;top:247px;width:180px;height:180px">
    <div class="result-photo__image result-photo__image--porch-after" role="img" aria-label="After photo: clean white covered porch and columns"></div>
    <div class="result-photo__label result-photo__label--red" style="height:30px;line-height:26px;font-size:15px">AFTER</div>
  </div>

  <div class="contact-band">
    <p class="contact-band__lines">212 Marsh Light Way St Augustine, FL 32080<br>hello@bluhavenwashco.example | www.bluhavenwashco.example</p>
    <span class="social-dot" style="left:691px" aria-label="Social profile link"></span>
    <span class="social-dot" style="left:757px" aria-label="Social profile link"></span>
  </div>
  <div class="call-tab">Call for Estimate: 555-013-4827</div>
</section>

</body>
</html>
```